Communication Business Card Design

We offer complete cabling solutions
Data Cabling,Fibre Optic, and Cabling Repairs fault finding
Security camera installation
TV Aerial installation
Security alarm installation
QWV

Industry/Entity Type

Business

Contact Information for Business Card

Threadmore Solutions
ABN 52 918 374 260
EMAIL threadmoresolutions.com.au
Mobile 0418362057
Rob Kesler

```html
<!DOCTYPE html>
<html lang="en">
<head>
<meta charset="utf-8">
<title>Threadmore Solutions – Business Card</title>
<link rel="stylesheet" href="https://fonts.googleapis.com/css2?family=Exo+2:wght@400;500;700&display=swap">
<style>
  :root {
    --page-bg: #e4e4e4;
    --card-black: #0b0c0d;
    --band-green: #7fc46f;
    --band-light: #f7fbf4;
    --band-tint: #b9dda9;
    --title-green: #86c878;
    --text-white: #ffffff;
    --text-dark: #1a1a1a;
    --bullet-green: #8fd27e;
  }
  * { margin: 0; padding: 0; box-sizing: border-box; }
  html, body { width: 1200px; height: 1000px; overflow: hidden; }
  body {
    background: var(--page-bg);
    font-family: "Exo 2", sans-serif;
    position: relative;
  }
  .card {
    position: absolute;
    width: 630px;
    height: 388px;
    background: var(--card-black);
    overflow: hidden;
  }
  .card-back { left: 119px; top: 130px; }
  .card-front { left: 487px; top: 538px; }
  .card-art { position: absolute; inset: 0; width: 630px; height: 388px; }

  .service-list {
    position: absolute;
    left: 0; right: 0; top: 274px;
    color: var(--text-white);
    font-size: 17.5px;
    font-weight: 500;
    text-align: center;
    line-height: 28.5px;
    letter-spacing: 0.2px;
  }
  .service { margin: 0 6px; white-space: nowrap; }
  .service::before {
    content: "\203A\203A";
    color: var(--bullet-green);
    font-size: 16px;
    font-weight: 700;
    letter-spacing: -1px;
    margin-right: 2px;
  }

  .company-name {
    position: absolute;
    left: 0; right: 0; top: 62px;
    text-align: center;
    color: var(--title-green);
    font-size: 34px;
    font-weight: 700;
    letter-spacing: 4px;
    text-transform: uppercase;
  }
  .person-name {
    position: absolute;
    left: 215px; width: 200px; top: 190px;
    text-align: center;
    color: var(--text-dark);
    font-size: 20px;
    font-weight: 700;
    letter-spacing: 1px;
    text-transform: uppercase;
  }
  .contact-list {
    position: absolute;
    left: 160px; width: 310px; top: 246px;
    text-align: center;
    color: var(--text-dark);
    font-size: 17px;
    font-weight: 500;
    line-height: 28.5px;
    list-style: none;
  }
  .phone-icon { width: 11px; height: 17px; vertical-align: -3px; margin-right: 2px; }
</style>
</head>
<body>

  <section class="card card-back" aria-label="Business card back">
    <svg class="card-art" viewBox="0 0 630 388">
      <defs>
        <radialGradient id="bandGlowBack" cx="0.42" cy="0.45" r="0.7">
          <stop offset="0" stop-color="var(--band-light)"/>
          <stop offset="0.6" stop-color="#e3f1db"/>
          <stop offset="1" stop-color="var(--band-tint)"/>
        </radialGradient>
        <linearGradient id="cableAreaBack" x1="0" y1="0" x2="1" y2="0">
          <stop offset="0" stop-color="#eef5ea"/>
          <stop offset="0.5" stop-color="#a9c9a3"/>
          <stop offset="1" stop-color="#4a5650"/>
        </linearGradient>
      </defs>
      <path d="M0,75 Q315,5 630,75 L630,263 Q315,187 0,263 Z" fill="url(#bandGlowBack)"/>
      <path d="M0,75 Q315,5 630,75" fill="none" stroke="var(--band-green)" stroke-width="5"/>
      <path d="M0,263 Q315,187 630,263" fill="none" stroke="var(--band-green)" stroke-width="5"/>
      <rect role="img" aria-label="Photo of a fibre optic cable with fanned out coloured strands"
            x="155" y="50" width="450" height="205" fill="url(#cableAreaBack)" opacity="0.75"/>
    </svg>
    <p class="service-list">
      <span class="service">Complete cabling solutions</span><span class="service">Data Cabling</span><span class="service">Fault finding</span><br>
      <span class="service">Security camera installation</span><span class="service">TV Aerial installation</span><span class="service">QWV</span><br>
      <span class="service">Security alarm installation</span><span class="service">Fibre Optic and Cabling Repairs</span>
    </p>
  </section>

  <section class="card card-front" aria-label="Business card front">
    <svg class="card-art" viewBox="0 0 630 388">
      <defs>
        <radialGradient id="bandGlowFront" cx="0.5" cy="0.5" r="0.7">
          <stop offset="0" stop-color="var(--band-light)"/>
          <stop offset="0.6" stop-color="#e6f3df"/>
          <stop offset="1" stop-color="var(--band-tint)"/>
        </radialGradient>
        <linearGradient id="cableAreaFront" x1="0" y1="1" x2="1" y2="0">
          <stop offset="0" stop-color="#8a8f90"/>
          <stop offset="0.5" stop-color="#a8c6bf"/>
          <stop offset="1" stop-color="#d4ecf4"/>
        </linearGradient>
      </defs>
      <path d="M0,125 Q315,195 630,125 L630,327 Q315,397 0,327 Z" fill="url(#bandGlowFront)"/>
      <path d="M0,125 Q315,195 630,125" fill="none" stroke="var(--band-green)" stroke-width="5"/>
      <path d="M0,327 Q315,397 630,327" fill="none" stroke="var(--band-green)" stroke-width="5"/>
      <rect role="img" aria-label="Photo of a fibre optic cable end with coloured tubes and blue strands"
            x="4" y="174" width="190" height="150" fill="url(#cableAreaFront)" opacity="0.75"/>
    </svg>
    <h1 class="company-name">Threadmore Solutions</h1>
    <h2 class="person-name">Rob Kesler</h2>
    <ul class="contact-list">
      <li>ABN 52 918 374 260</li>
      <li>@threadmoresolutions.com.au</li>
      <li><svg class="phone-icon" viewBox="0 0 11 17" aria-hidden="true"><rect x="0.5" y="0.5" width="10" height="16" rx="1.5" fill="none" stroke="#1a1a1a"/><rect x="2" y="2.5" width="7" height="6" fill="#1a1a1a"/><rect x="2" y="10" width="7" height="5" fill="#1a1a1a" opacity="0.6"/></svg>0418 362 057</li>
    </ul>
  </section>

</body>
</html>
```